Healthcare IT firm needs classy and unique business care design

We need a business card design that incorporates our new logo design (attached) Prefer a purple based designed. I would really love to see something utilizing the "3D" version of the logo (purple on the reflective wall). I want something a little more than my logo printed along with a person's detailed contact information.
Contact Information for Business Card
Want something polished, professional, and a little unique in the design.
Colors
6b449b
Requirements
Must have
- Please use similar font as the logo design
Nice to have
- Would like to see the 3d version of my logo incorporated into the design.

```html
<!DOCTYPE html>
<html lang="en">
<head>
<meta charset="utf-8">
<title>Veralink Health Systems — Business Card</title>
<link href="https://fonts.googleapis.com/css2?family=Montserrat:wght@700&family=Work+Sans:wght@400;500;600&display=swap" rel="stylesheet">
<style>
  :root {
    --stage: #1c1c1e;
    --card: #2a2a2b;
    --card-edge: #333335;
    --purple: #6b449b;
    --purple-bright: #8757c4;
    --silver: #b9b9bd;
    --white: #f2f2f2;
  }
  html, body {
    margin: 0;
    padding: 0;
    width: 1200px;
    height: 900px;
    overflow: hidden;
    background: var(--stage);
  }
  .canvas {
    position: relative;
    width: 1200px;
    height: 900px;
    font-family: "Work Sans", sans-serif;
  }
  .card {
    position: absolute;
    left: 250px;
    width: 700px;
    height: 400px;
    background: linear-gradient(135deg, #262627 0%, var(--card) 55%, #303031 100%);
    border: 1px solid var(--card-edge);
    box-sizing: border-box;
  }
  .card--front { top: 38px; }
  .card--back { top: 462px; }

  /* Front */
  .front-brand {
    position: absolute;
    top: 150px;
    left: 0;
    width: 100%;
    text-align: center;
    font-family: "Work Sans", sans-serif;
    font-weight: 600;
    font-size: 48px;
    letter-spacing: 1px;
    color: var(--silver);
  }
  .front-url {
    position: absolute;
    top: 318px;
    left: 0;
    width: 100%;
    text-align: center;
    font-size: 17px;
    letter-spacing: 1px;
    color: var(--white);
  }

  /* Back */
  .back-brand {
    position: absolute;
    top: 158px;
    left: 48px;
    width: 300px;
    font-weight: 600;
    font-size: 34px;
    line-height: 1.15;
    color: var(--purple-bright);
  }
  .divider {
    position: absolute;
    left: 372px;
    top: 92px;
    width: 3px;
    height: 216px;
    background: var(--purple);
  }
  .contact {
    position: absolute;
    left: 404px;
    top: 92px;
    color: var(--white);
  }
  .contact__name {
    font-family: "Montserrat", sans-serif;
    font-weight: 700;
    font-size: 27px;
    color: var(--purple-bright);
    margin: 0;
    letter-spacing: 1px;
  }
  .contact__role {
    font-size: 17px;
    margin: 0 0 20px;
    letter-spacing: 1px;
  }
  .contact__address {
    font-size: 17px;
    line-height: 1.3;
    margin: 0 0 8px;
    letter-spacing: 1px;
  }
  .contact__row {
    display: flex;
    align-items: center;
    gap: 10px;
    font-size: 17px;
    letter-spacing: 1px;
    line-height: 1.55;
  }
  .contact__row svg { width: 14px; height: 14px; flex: none; }
  .accent { color: var(--purple-bright); }
</style>
</head>
<body>
<div class="canvas">

  <section class="card card--front">
    <div class="front-brand">Veralink Health Systems</div>
    <div class="front-url">www.veralink.com</div>
  </section>

  <section class="card card--back">
    <div class="back-brand">Veralink<br>Health Systems</div>
    <div class="divider"></div>
    <div class="contact">
      <p class="contact__name">Daniel Reyes</p>
      <p class="contact__role">Founder</p>
      <p class="contact__address">480 Harbor View Ave.<br>Coral Point, FL 33100</p>
      <div class="contact__row">
        <svg viewBox="0 0 16 16" aria-hidden="true"><path d="M4 1.5 6 4.5 4.8 6c.8 1.9 2.3 3.4 4.2 4.2L10.5 9l3 2-1 2.5C7.5 13.5 2.5 8.5 2.5 3.5z" fill="var(--purple-bright)"/></svg>
        <span>555-014-2290</span>
      </div>
      <div class="contact__row">
        <svg viewBox="0 0 16 16" aria-hidden="true"><rect x="1.5" y="3.5" width="13" height="9" fill="none" stroke="var(--purple-bright)" stroke-width="1.4"/><path d="M1.5 3.5 8 9l6.5-5.5" fill="none" stroke="var(--purple-bright)" stroke-width="1.4"/></svg>
        <span>info@veralink.com</span>
      </div>
      <div class="contact__row">
        <svg viewBox="0 0 16 16" aria-hidden="true"><circle cx="8" cy="8" r="6.5" fill="none" stroke="var(--purple-bright)" stroke-width="1.4"/><ellipse cx="8" cy="8" rx="2.8" ry="6.5" fill="none" stroke="var(--purple-bright)" stroke-width="1.2"/><path d="M1.5 8h13" stroke="var(--purple-bright)" stroke-width="1.2"/></svg>
        <span>www.<span class="accent">veralink</span>.com</span>
      </div>
    </div>
  </section>

</div>
</body>
</html>
```